Letterhead Design

We are a physical security and protective intelligence firm based in regional NSW, Australia. We are in need of a professionally designed letter head/ document for our company Valdrin Security. Ref. www.valdrinsecurity.com.au for detailed company information. MUST include Master Licence and ABN details.

Target Market(s)

corporate business, celebrities, property managers, entertainment professionals

Industry/Entity Type

Security

Requirements
Must have
• Must look sharp, professional and cutting edge. Think 482, Hollow Watch, QR8/9 and NOT the movie known as "Gus Fenwick Arcade Warden". :-)
Should not have
• Please NO cheesy security guards standing around in uniform. Think protective intelligence and counter terrorism operations. We do not wish to convey an image of a guard company, we offer this service but it is not what we aim to promote. Seek to achieve a higher level approach... elite as opposed to "the usual" guard services etc.

```html
<!DOCTYPE html>
<html lang="en">
<head>
<meta charset="utf-8">
<title>Valdrin Security Letterhead</title>
<link href="https://fonts.googleapis.com/css2?family=Source+Sans+3:wght@400;500;600&display=swap" rel="stylesheet">
<style>
  :root {
    --backdrop: #4a4a4b;
    --paper: #ffffff;
    --banner: #0b0c0d;
    --accent: #e3141b;
    --ink: #1a1a1a;
    --on-dark: #ffffff;
  }
  html, body {
    margin: 0;
    padding: 0;
    width: 1200px;
    height: 1000px;
    overflow: hidden;
    background: var(--backdrop);
    font-family: "Source Sans 3", "Myriad Pro", Arial, sans-serif;
  }
  .letterhead {
    position: absolute;
    left: 294px;
    top: 84px;
    width: 602px;
    height: 846px;
    background: var(--paper);
  }
  .header-banner {
    position: absolute;
    left: 375px;
    top: 0;
    width: 175px;
    height: 90px;
  }
  .header-banner svg {
    position: absolute;
    inset: 0;
  }
  .brand {
    position: absolute;
    left: 0;
    right: 0;
    top: 37px;
    text-align: center;
    color: var(--on-dark);
  }
  .brand-name {
    display: block;
    font-size: 14px;
    font-weight: 500;
    letter-spacing: 0.3px;
    line-height: 1;
  }
  .brand-tagline {
    display: block;
    margin-top: 5px;
    font-size: 5.5px;
    font-weight: 400;
    line-height: 1;
  }
  .contact-block {
    position: absolute;
    left: 23px;
    top: 728px;
    color: var(--ink);
    font-size: 9px;
    line-height: 12.4px;
  }
  .contact-company {
    color: var(--accent);
    font-size: 13.5px;
    line-height: 18px;
    margin: 0 0 1px;
    font-weight: 400;
  }
  .contact-list {
    list-style: none;
    margin: 0;
    padding: 0;
  }
  .contact-label {
    color: var(--accent);
  }
</style>
</head>
<body>
  <main class="letterhead">
    <header class="header-banner">
      <svg width="175" height="90" viewBox="0 0 175 90" aria-hidden="true">
        <polygon points="0,0 175,0 175,69 87.5,90 0,69" fill="var(--banner)"/>
      </svg>
      <div class="brand">
        <span class="brand-name">VALDRIN SECURITY</span>
        <span class="brand-tagline">Precision in the Craft of Protection</span>
      </div>
    </header>

    <footer class="contact-block">
      <h1 class="contact-company">Valdrin Security</h1>
      <ul class="contact-list">
        <li><span class="contact-label">Tel:</span> (02) 5550 1847 or 0400 555 219</li>
        <li><span class="contact-label">Email:</span> office@ValdrinSecurity.com.au</li>
        <li><span class="contact-label">Web:</span>&nbsp; www.valdrinsecurity.com.au</li>
        <li><span class="contact-label">SPIA Member:</span> 00 07 31 58</li>
        <li><span class="contact-label">ABN:</span> 51 824 309 117</li>
        <li><span class="contact-label">Master Licence:</span> 40917 3356</li>
        <li>Tamberra New South Wales Australia, 2399</li>
      </ul>
    </footer>
  </main>
</body>
</html>
```